half page print advert for glossy wedding brochure

I need an advert designed for a glossy magazine - the size is 140mm wide by 195mm high.

this is a high-quality brochure handed out to brides who visit the location and I need them to consider booking me for their wedding video.My logo is attached as is the advert I did for myself last time (that's why I'm paying this time...)

every bride thinks about flowers and photography and a cake but only about half even consider video and only about 35% of weddings in Australia book video. that's why I came up with catch phrases like "you spend a long time planning your wedding - how do you plan to remember it?" - "the only way to truly relive the day is to record the sights & sound of your wedding as they happened - a truly moving image" They seem to get brides thinking but it's up to you what you include- you may come up with something completely different - I don't care what it is or says, as long as it works

I need an advert that makes the bride stop and think about getting a wedding video, that makes her want to check out our website & facebook page or call or email us.

Target Market(s)

Brides, engaged couples

Industry/Entity Type

Wedding

Requirements
Must have
• logo, contact details - website, email, facebook, phone
Nice to have
• something that stands out, with a modern look to attract that age group. You do not have to use the catch phrases I mentioned, they are just to give you an idea,

```html
<!DOCTYPE html>
<html lang="en">
<head>
<meta charset="utf-8">
<title>Keepsake Reel – Wedding Film Advert</title>
<link rel="stylesheet" href="https://fonts.googleapis.com/css2?family=Lato:wght@400;700;900&display=swap">
<style>
  :root {
    --page-bg: #e9eaec;
    --sky-blue: #0fa3dc;
    --deep-blue: #0a86c2;
    --pale-blue: #bfe6f6;
    --sun-yellow: #f7c315;
    --navy: #1b3557;
    --ink: #1d1d1f;
    --white: #ffffff;
    --mist: #f4f5f6;
    --silver: #d9dbde;
  }
  * { margin: 0; padding: 0; box-sizing: border-box; }
  html, body {
    width: 1020px; height: 1200px; overflow: hidden;
    background: var(--page-bg);
    font-family: "Lato", Arial, sans-serif;
  }
  .advert {
    position: absolute; left: 100px; top: 29px;
    width: 820px; height: 1142px;
    background: var(--white);
    overflow: hidden;
    box-shadow: 0 4px 18px rgba(0,0,0,0.18);
  }
  .advert-shapes { position: absolute; inset: 0; }
  .headline {
    position: absolute; top: 56px; left: 0; width: 100%;
    text-align: center; color: var(--white);
    font-weight: 700;
  }
  .headline-main { font-size: 37px; line-height: 54px; letter-spacing: 0.5px; }
  .headline-sub { font-size: 29px; margin-top: 6px; }
  .couple-photo {
    position: absolute; left: 117px; top: 262px;
    width: 626px; height: 440px;
    background: linear-gradient(180deg, #122033 0%, #1e2f48 55%, #e7e9ec 72%, #f6f7f8 100%);
  }
  .tagline {
    position: absolute; left: 70px; top: 712px;
    font-size: 20px; line-height: 28px; color: var(--ink);
  }
  .contact {
    position: absolute; left: 60px; top: 960px; color: var(--navy);
  }
  .contact-title { font-size: 34px; font-weight: 700; margin-bottom: 14px; }
  .contact-list { list-style: none; }
  .contact-item {
    display: flex; align-items: center; gap: 12px;
    font-size: 22px; line-height: 33px; color: var(--ink);
  }
  .contact-icon { width: 18px; height: 18px; flex: none; }
  .brand {
    position: absolute; left: 470px; top: 1060px;
    display: flex; align-items: center; gap: 12px;
  }
  .brand-dot { width: 26px; height: 26px; border-radius: 50%; background: var(--sky-blue); }
  .brand-name { font-size: 40px; font-weight: 900; color: var(--navy); letter-spacing: 0.5px; }
</style>
</head>
<body>
<main class="advert">
  <svg class="advert-shapes" width="820" height="1142" viewBox="0 0 820 1142" aria-hidden="true">
    <defs>
      <linearGradient id="skyFill" x1="0" y1="0" x2="1" y2="1">
        <stop offset="0" stop-color="#0b8fcc"/>
        <stop offset="0.5" stop-color="#16b2ea"/>
        <stop offset="1" stop-color="#0a86c2"/>
      </linearGradient>
      <linearGradient id="mistFill" x1="0" y1="0" x2="0" y2="1">
        <stop offset="0" stop-color="#ffffff"/>
        <stop offset="1" stop-color="#d9dbde"/>
      </linearGradient>
    </defs>
    <path d="M0 0 H820 V300 C560 300 280 320 0 470 Z" fill="var(--pale-blue)"/>
    <path d="M0 0 H820 V232 C580 225 300 270 0 440 Z" fill="url(#skyFill)"/>
    <path d="M0 1142 V985 C260 880 540 840 820 848 V1142 Z" fill="url(#mistFill)"/>
    <path d="M0 985 C260 880 540 840 820 848 V818 C540 808 260 850 0 975 Z" fill="var(--sun-yellow)"/>
    <path d="M0 968 C260 840 540 800 820 806" fill="none" stroke="var(--deep-blue)" stroke-width="10"/>
  </svg>

  <header class="headline">
    <div class="headline-main">YOU SPEND A LONG TIME<br>PLANNING YOUR WEDDING .....</div>
    <div class="headline-sub">how do you plan to REMEMBER IT?</div>
  </header>

  <div class="couple-photo" role="img" aria-label="Photo of a smiling couple on a white sofa in front of a television screen"></div>

  <p class="tagline">The only way to truly relive<br>the day is to record the sights &amp; sound of<br>your wedding as they happened<br>- a truly moving image</p>

  <section class="contact">
    <h2 class="contact-title">Contact Today</h2>
    <ul class="contact-list">
      <li class="contact-item">
        <svg class="contact-icon" viewBox="0 0 20 20"><circle cx="10" cy="10" r="8.5" fill="none" stroke="var(--sky-blue)" stroke-width="1.6"/><path d="M7 5.5l1.6 2.2-1 1.2c.7 1.4 1.7 2.4 3.1 3.1l1.2-1 2.2 1.6-.9 1.6c-3.6-.5-6.4-3.3-6.9-6.9z" fill="var(--sky-blue)"/></svg>
        <span>0400 186 245</span>
      </li>
      <li class="contact-item">
        <svg class="contact-icon" viewBox="0 0 20 20"><rect x="1.5" y="4" width="17" height="12" fill="none" stroke="var(--sky-blue)" stroke-width="1.6"/><path d="M1.5 4l8.5 7 8.5-7" fill="none" stroke="var(--sky-blue)" stroke-width="1.6"/></svg>
        <span>hello@keepsakereel.com.au</span>
      </li>
      <li class="contact-item">
        <svg class="contact-icon" viewBox="0 0 20 20"><circle cx="10" cy="10" r="8.5" fill="none" stroke="var(--sky-blue)" stroke-width="1.6"/><ellipse cx="10" cy="10" rx="3.6" ry="8.5" fill="none" stroke="var(--sky-blue)" stroke-width="1.4"/><path d="M1.5 10h17" stroke="var(--sky-blue)" stroke-width="1.4"/></svg>
        <span>www.keepsakereel.com.au</span>
      </li>
    </ul>
  </section>

  <div class="brand">
    <span class="brand-dot"></span>
    <span class="brand-name">KEEPSAKE REEL</span>
  </div>
</main>
</body>
</html>
```